Wine label design for my wife. Wine called "The Mirabel"

I need a wine label face lift of one of my premium wines in my collection. My wine sells in Harbor Lark's all over the States. My current label is called The Mirabel (my wife's name) and the illustration of her eyes is done by a well know artist from South Africa. I do not have to use this illustration and therefor I attached several pictures of her and her eyes, even when she was a little girl. The wine's also made in South Africa. This is a premium wine that we only sell 2000 bottles per year. The wine sells at 60 usd per bottle, The current label is too white. I also think her eyes should look more at the person buying it, than away from them.

Target Market(s)

Top end wine buyers

Font styles to use
Decorative
Script

Requirements
Must have
• 'The Mirabel' must be on the label
An illustration must be on the label
Basically all the info that's on the current label must be on by law. As per Sample
Nice to have
• Maybe some ideas of her whole face?
Should not have
• any gold colour

```html
<!DOCTYPE html>
<html lang="en">
<head>
<meta charset="utf-8">
<title>The Mirabel — Sauvignon 2017 Label</title>
<link rel="stylesheet" href="https://fonts.googleapis.com/css2?family=Pinyon+Script&family=Libre+Baskerville:wght@400;700&display=swap">
<style>
  :root {
    --label-grey: #c6c6c6;
    --label-grey-light: #cdcdcd;
    --label-grey-deep: #bfbfbf;
    --emboss-white: #fbfbfb;
    --emboss-shadow: rgba(80, 80, 80, 0.5);
    --emboss-highlight: rgba(255, 255, 255, 0.7);
    --varietal-taupe: #857d72;
    --portrait-white: #f3f3f3;
    --portrait-soft: #e6e6e6;
  }

  html, body {
    margin: 0;
    padding: 0;
    width: 1200px;
    height: 670px;
    overflow: hidden;
    background: var(--label-grey);
  }

  .wine-label {
    position: relative;
    width: 1200px;
    height: 670px;
    overflow: hidden;
    background: linear-gradient(160deg, var(--label-grey-light) 0%, var(--label-grey) 55%, var(--label-grey-deep) 100%);
  }

  .signature-flourish {
    position: absolute;
    left: 40px;
    top: 110px;
    width: 590px;
    height: 420px;
    background: radial-gradient(ellipse at 50% 55%, rgba(225, 225, 225, 0.4) 0%, rgba(225, 225, 225, 0) 70%);
  }

  .portrait {
    position: absolute;
    left: 0;
    top: 0;
    width: 1200px;
    height: 670px;
  }

  .wine-name {
    position: absolute;
    left: 54px;
    top: 252px;
    margin: 0;
    font-family: "Pinyon Script", cursive;
    font-weight: 400;
    font-size: 112px;
    line-height: 1;
    color: var(--emboss-white);
    white-space: nowrap;
    text-shadow: 1px 2px 2px var(--emboss-shadow), -1px -1px 0 var(--emboss-highlight);
  }

  .varietal-vintage {
    position: absolute;
    left: 138px;
    top: 382px;
    margin: 0;
    font-family: "Libre Baskerville", serif;
    font-weight: 700;
    font-size: 41px;
    letter-spacing: 0.5px;
    line-height: 1;
    color: var(--varietal-taupe);
    white-space: nowrap;
    text-shadow: 1px 1px 1px rgba(60, 55, 50, 0.35), -1px -1px 0 var(--emboss-highlight);
  }

  .producer {
    position: absolute;
    left: 151px;
    top: 576px;
    margin: 0;
    font-family: "Libre Baskerville", serif;
    font-weight: 400;
    font-size: 40px;
    font-variant: small-caps;
    line-height: 1;
    color: var(--emboss-white);
    white-space: nowrap;
    text-shadow: 1px 1px 2px var(--emboss-shadow);
  }
</style>
</head>
<body>
  <main class="wine-label">
    <div class="signature-flourish" role="img" aria-label="Faint handwritten signature flourish behind the wine name"></div>
    <svg class="portrait" viewBox="0 0 1200 670" role="img" aria-label="Embossed white portrait illustration of a smiling woman, head and shoulders">
      <defs>
        <linearGradient id="portrait-fill" x1="0" y1="0" x2="1" y2="1">
          <stop offset="0" stop-color="var(--portrait-white)"/>
          <stop offset="1" stop-color="var(--portrait-soft)"/>
        </linearGradient>
        <filter id="emboss-edge" x="-5%" y="-5%" width="110%" height="110%">
          <feDropShadow dx="2" dy="3" stdDeviation="2" flood-color="#6a6a6a" flood-opacity="0.45"/>
        </filter>
      </defs>
      <path class="portrait-area" filter="url(#emboss-edge)" fill="url(#portrait-fill)"
            d="M 600 670 C 610 600 640 520 680 470 C 700 440 705 400 700 330 C 705 220 730 110 790 40 C 820 5 870 -5 920 0 L 990 0 C 1040 40 1060 150 1050 260 C 1045 330 1020 390 980 430 C 950 460 930 480 925 490 C 990 530 1090 560 1160 600 L 1200 625 L 1200 670 Z"/>
    </svg>
    <h1 class="wine-name">The Mirabel</h1>
    <p class="varietal-vintage">SAUVIGNON 2017</p>
    <p class="producer">Peter Hollis Wine</p>
  </main>
</body>
</html>
```